Natural Cosmetics need a Packaging Design

We need a PACKAGING design for labels on hand/body wash bottles and soap paper boxes.
We target at high end markets.
We expect a contemporary and trendy design.
We don't need a separate logo. The brand name "Va Mirel" acts as the logo.
We want a modern and classic font for "Va Mirel".
Please see attached pictures for packaging samples.

Industry/Entity Type

Cosmetics

Requirements
Should not have
• a separate logo from the brand name

```html
<!DOCTYPE html>
<html lang="fr">
<head>
<meta charset="utf-8">
<title>Va Mirel – Nuage de Pétales packaging</title>
<link rel="stylesheet" href="https://fonts.googleapis.com/css2?family=Great+Vibes&family=Raleway:wght@300&family=Oswald:wght@300&family=Noto+Serif:ital@1&display=swap">
<style>
  :root{
    --backdrop:#d0cde6;
    --bottle:#939396;
    --lilac:#b3a5d3;
    --lilac-soft:#e9e4f4;
    --text-soft:#a896d0;
    --text-blue:#3f6fc0;
    --text-dark:#4d4178;
    --sky:#8fd7f5;
    --sky-soft:#e6f5fc;
    --pink:#e85aa0;
    --white:#ffffff;
  }
  *{margin:0;padding:0;box-sizing:border-box}
  html,body{width:1200px;height:848px;overflow:hidden;background:var(--backdrop)}
  .board{position:relative;width:1200px;height:848px}
  .bottles{position:absolute;left:0;top:0;width:1200px;height:848px}
  .bottles path{fill:var(--bottle)}

  .label{position:absolute;width:474px;height:290px;transform-origin:0 0;overflow:hidden;
    --accent:var(--lilac);--accent-soft:var(--lilac-soft);
    --title-a:var(--text-blue);--title-b:var(--text-dark);
    --line-a:var(--text-soft);--line-b:var(--text-blue)}
  .label--sky{--accent:var(--sky);--accent-soft:var(--sky-soft);
    --title-a:var(--sky);--title-b:var(--pink);
    --line-a:var(--pink);--line-b:var(--text-blue)}
  .label__pattern{position:absolute;inset:0;background:linear-gradient(135deg,var(--accent-soft),var(--white) 50%,var(--accent-soft))}
  .label__card{position:absolute;left:46px;top:84px;width:382px;height:170px;background:var(--white);
    box-shadow:0 0 14px rgba(120,100,170,.35);text-align:center}
  .label__brand{position:absolute;left:166px;top:0;width:142px;height:119px;background:var(--accent);
    display:flex;flex-direction:column;align-items:center;padding-top:28px}
  .label__brand-name{font-family:"Raleway",sans-serif;font-weight:300;font-size:28px;color:var(--white);letter-spacing:.5px;line-height:1;white-space:nowrap}
  .label__brand-dot{width:18px;height:18px;border:2px solid var(--title-a);border-radius:50%;margin-top:22px}
  .label__title{position:absolute;left:0;right:0;top:46px;font-family:"Great Vibes",cursive;font-weight:400;font-size:36px;line-height:1;white-space:nowrap;
    background:linear-gradient(90deg,var(--title-a),var(--title-b));-webkit-background-clip:text;background-clip:text;color:transparent}
  .label__tagline{position:absolute;left:0;right:0;top:94px;font-family:"Oswald",sans-serif;font-weight:300;font-size:7.5px;color:var(--text-dark);white-space:nowrap}
  .label__steps{position:absolute;left:0;right:0;top:116px;list-style:none;font-family:"Noto Serif",serif;font-style:italic;font-size:7px;line-height:9.4px;white-space:nowrap}
  .fr{color:var(--line-a)}
  .en{color:var(--line-b)}
  .label__band{position:absolute;left:0;right:0;top:270px;height:20px;background:var(--accent);
    font-family:"Oswald",sans-serif;font-weight:300;font-size:6px;color:var(--white);text-align:center;line-height:20px}

  .label--box{left:116px;top:22px}
  .label--pump{left:204px;top:616px;transform:scale(.633)}
  .label--tall{left:643px;top:377px;transform:scale(.452)}
  .label--tall-sky{left:954px;top:377px;transform:scale(.452)}
</style>
</head>
<body>
<main class="board">
  <svg class="bottles" viewBox="0 0 1500 1060" aria-hidden="true">
    <path d="M340 462 Q400 440 456 448 L456 525 L508 525 L508 600 Q620 640 630 760 L630 1000 Q630 1045 590 1045 L295 1045 Q255 1045 255 1000 L255 760 Q265 640 375 600 L375 525 L430 525 L430 470 Q380 468 345 478 Z"/>
    <path d="M770 182 Q880 170 990 182 L992 205 L990 275 L1000 275 L1000 340 Q1072 370 1072 440 L1072 1020 Q1072 1045 1045 1045 L830 1045 Q804 1045 804 1020 L804 440 Q804 370 868 340 L868 275 L965 275 L965 200 Q880 195 785 205 Z"/>
    <path d="M1158 182 Q1268 170 1378 182 L1380 205 L1378 275 L1388 275 L1388 340 Q1460 370 1460 440 L1460 1020 Q1460 1045 1433 1045 L1218 1045 Q1192 1045 1192 1020 L1192 440 Q1192 370 1256 340 L1256 275 L1353 275 L1353 200 Q1268 195 1173 205 Z"/>
  </svg>

  <section class="label label--box">
    <div class="label__pattern" role="img" aria-label="Fine line drawing of lilies and leaves in lilac"></div>
    <div class="label__card">
      <h1 class="label__title">Nuage de Pétales</h1>
      <p class="label__tagline">UNE MOUSSE LÉGÈRE POUR TOUT LE CORPS! A LIGHT FOAM FOR ALL THE BODY!</p>
      <ul class="label__steps">
        <li><span class="fr">Comment l'utiliser ?</span> <span class="en">How to use it?</span></li>
        <li><span class="fr">1. Faire mousser dans la main.</span> <span class="en">Work a lather in your palm</span></li>
        <li><span class="fr">2. Appliquer sur le visage et le corps</span></li>
        <li><span class="en">Apply over your face and your body</span></li>
        <li><span class="fr">3. Rincer à l'eau claire.</span> <span class="en">Rinse off</span></li>
      </ul>
    </div>
    <div class="label__brand"><span class="label__brand-name">Va Mirel</span><span class="label__brand-dot"></span></div>
    <div class="label__band">MADE IN FRANCE / FABRIQUÉ EN FRANCE</div>
  </section>

  <section class="label label--pump">
    <div class="label__pattern" role="img" aria-label="Fine line drawing of lilies and leaves in lilac"></div>
    <div class="label__card">
      <h2 class="label__title">Nuage de Pétales</h2>
      <p class="label__tagline">UNE MOUSSE LÉGÈRE POUR TOUT LE CORPS! A LIGHT FOAM FOR ALL THE BODY!</p>
      <ul class="label__steps">
        <li><span class="fr">Comment l'utiliser ?</span> <span class="en">How to use it?</span></li>
        <li><span class="fr">1. Faire mousser dans la main.</span> <span class="en">Work a lather in your palm</span></li>
        <li><span class="fr">2. Appliquer sur le visage et le corps</span></li>
        <li><span class="en">Apply over your face and your body</span></li>
        <li><span class="fr">3. Rincer à l'eau claire.</span> <span class="en">Rinse off</span></li>
      </ul>
    </div>
    <div class="label__brand"><span class="label__brand-name">Va Mirel</span><span class="label__brand-dot"></span></div>
    <div class="label__band">MADE IN FRANCE / FABRIQUÉ EN FRANCE</div>
  </section>

  <section class="label label--tall">
    <div class="label__pattern" role="img" aria-label="Fine line drawing of lilies and leaves in lilac"></div>
    <div class="label__card">
      <h2 class="label__title">Nuage de Pétales</h2>
      <p class="label__tagline">UNE MOUSSE LÉGÈRE POUR TOUT LE CORPS! A LIGHT FOAM FOR ALL THE BODY!</p>
      <ul class="label__steps">
        <li><span class="fr">Comment l'utiliser ?</span> <span class="en">How to use it?</span></li>
        <li><span class="fr">1. Faire mousser dans la main.</span> <span class="en">Work a lather in your palm</span></li>
        <li><span class="fr">2. Appliquer sur le visage et le corps</span></li>
        <li><span class="en">Apply over your face and your body</span></li>
        <li><span class="fr">3. Rincer à l'eau claire.</span> <span class="en">Rinse off</span></li>
      </ul>
    </div>
    <div class="label__brand"><span class="label__brand-name">Va Mirel</span><span class="label__brand-dot"></span></div>
    <div class="label__band">MADE IN FRANCE / FABRIQUÉ EN FRANCE</div>
  </section>

  <section class="label label--tall-sky label--sky">
    <div class="label__pattern" role="img" aria-label="Fine line drawing of lilies and leaves in pale sky blue"></div>
    <div class="label__card">
      <h2 class="label__title">Nuage de Pétales</h2>
      <p class="label__tagline">UNE MOUSSE LÉGÈRE POUR TOUT LE CORPS! A LIGHT FOAM FOR ALL THE BODY!</p>
      <ul class="label__steps">
        <li><span class="fr">Comment l'utiliser ?</span> <span class="en">How to use it?</span></li>
        <li><span class="fr">1. Faire mousser dans la main.</span> <span class="en">Work a lather in your palm</span></li>
        <li><span class="fr">2. Appliquer sur le visage et le corps</span></li>
        <li><span class="en">Apply over your face and your body</span></li>
        <li><span class="fr">3. Rincer à l'eau claire.</span> <span class="en">Rinse off</span></li>
      </ul>
    </div>
    <div class="label__brand"><span class="label__brand-name">Va Mirel</span><span class="label__brand-dot"></span></div>
    <div class="label__band">MADE IN FRANCE / FABRIQUÉ EN FRANCE</div>
  </section>
</main>
</body>
</html>
```